UK Supplement Company Needs a Label for Diet Protein Powder

We need a new, modern and fresh design for our Diet Protein Powder. Our protein powder is packaged in black plastic tubs (photo attached) and needs an attractive label. We would like to see designs that grab attention and look professional. We're very open to ideas. The label should be 88mm x 365mm. We also prefer PSD format where possible. These alterations could be made once your design is chosen. Have attached photo of our shake ingredients/benefits.
Updates

Need extra days to review

Target Market(s)

Slimmers

Industry/Entity Type

Health And Wellness

Font styles to use
Serif
Sans Serif

Colors

Designer to choose colors to be used in the design.

Requirements
Must have
• Clean, Modern and Professional Look. Eye catching. The flavour, we offer 6 flavours so this must be something we can edit (Flavours are Banana, Chocolate, Chocolate Mint, Strawberry, Toffee and Vanilla).
Nice to have
• Our logo, this can be KELVORA Nutrition or just KELVORA. Our logo files are attached.
Should not have
• We do not want to see people (faces or bodies) on the design.

```html
<!DOCTYPE html>
<html lang="en">
<head>
<meta charset="utf-8">
<title>KELVORA Nutrition – Low Calorie Protein Shake Label</title>
<link href="https://fonts.googleapis.com/css2?family=Montserrat:wght@400;500;700;800&family=Roboto+Condensed:wght@400;700&display=swap" rel="stylesheet">
<style>
  :root {
    --red: #d7262f;
    --red-deep: #b51d25;
    --red-light: #e04a52;
    --ink: #1c1c1c;
    --tab-grey: #3a3a3a;
    --white: #ffffff;
    --blush: #f6c9cb;
    --canvas: #f4f4f4;
  }
  html, body {
    margin: 0;
    width: 1200px;
    height: 1200px;
    overflow: hidden;
    background: var(--canvas);
  }
  .canvas {
    position: relative;
    width: 1200px;
    height: 1200px;
    display: flex;
    align-items: center;
    justify-content: center;
  }
  .label {
    width: 1100px;
    height: 740px;
    display: block;
    box-shadow: 0 10px 30px rgba(0,0,0,0.12);
  }
  .flavour-small { font: 500 15px "Montserrat", sans-serif; fill: var(--white); letter-spacing: 1px; }
  .flavour-big { font: 700 21px "Montserrat", sans-serif; fill: var(--white); letter-spacing: 2px; }
  .brand-name { font: 800 82px "Montserrat", sans-serif; fill: var(--white); }
  .brand-sub { font: 800 17px "Montserrat", sans-serif; fill: var(--white); letter-spacing: 9px; }
  .claim { font: 500 36px "Montserrat", sans-serif; fill: var(--ink); }
  .product { font: 800 58px "Montserrat", sans-serif; fill: var(--red); }
  .stat-num { font: 700 30px "Roboto Condensed", sans-serif; fill: var(--ink); }
  .stat-label { font: 700 8px "Roboto Condensed", sans-serif; fill: var(--ink); }
  .stat-foot { font: 400 14px "Roboto Condensed", sans-serif; fill: var(--white); }
  .tab-text { font: 500 15px "Montserrat", sans-serif; fill: var(--white); }
</style>
</head>
<body>
<main class="canvas">
  <svg class="label" viewBox="0 0 1100 740" xmlns="http://www.w3.org/2000/svg">
    <defs>
      <linearGradient id="lowerFade" x1="0" y1="0" x2="0" y2="1">
        <stop offset="0" stop-color="var(--white)"/>
        <stop offset="0.7" stop-color="var(--white)"/>
        <stop offset="1" stop-color="var(--blush)"/>
      </linearGradient>
      <linearGradient id="bandShade" x1="0" y1="0" x2="1" y2="0">
        <stop offset="0" stop-color="var(--red-deep)"/>
        <stop offset="0.5" stop-color="var(--red)"/>
        <stop offset="1" stop-color="var(--red-deep)"/>
      </linearGradient>
      <radialGradient id="berryTone" cx="0.5" cy="0.5" r="0.5">
        <stop offset="0" stop-color="#e2393f"/>
        <stop offset="0.7" stop-color="#c81e27"/>
        <stop offset="1" stop-color="#c81e27" stop-opacity="0"/>
      </radialGradient>
    </defs>

    <rect class="lower-panel" x="0" y="0" width="1100" height="740" fill="url(#lowerFade)"/>
    <rect class="top-band" x="0" y="0" width="1100" height="380" fill="url(#bandShade)"/>

    <path class="bowl" d="M 380 378 Q 550 500 720 378 Z" fill="var(--red-deep)"/>
    <path class="bowl-rim" d="M 410 380 Q 550 470 690 380" fill="none" stroke="var(--white)" stroke-width="5"/>
    <path class="bowl-inner" d="M 430 380 Q 550 455 670 380 Z" fill="var(--red)"/>

    <ellipse class="fruit-image" cx="550" cy="340" rx="115" ry="80" fill="url(#berryTone)" role="img" aria-label="Photo of fresh strawberries"/>

    <g class="flavour-tab">
      <path d="M 468 0 L 632 0 L 622 62 L 478 62 Z" fill="var(--red-deep)"/>
      <path d="M 476 0 L 476 4 L 484 56 L 616 56 L 624 4 L 624 0" fill="none" stroke="var(--white)" stroke-width="2"/>
      <text class="flavour-small" x="550" y="22" text-anchor="middle">STRAWBERRY</text>
      <text class="flavour-big" x="550" y="45" text-anchor="middle">FLAVOUR</text>
    </g>

    <g class="brand">
      <text class="brand-name" x="550" y="178" text-anchor="middle">KELVORA</text>
      <text class="brand-sub" x="555" y="216" text-anchor="middle">NUTRITION</text>
    </g>

    <text class="claim" x="550" y="493" text-anchor="middle">LOW CALORIE</text>
    <line x1="370" y1="512" x2="730" y2="512" stroke="var(--red)" stroke-width="1.5"/>
    <text class="product" x="550" y="578" text-anchor="middle">PROTEIN SHAKE</text>
    <line x1="360" y1="598" x2="740" y2="598" stroke="var(--red)" stroke-width="1.5"/>

    <g class="stats">
      <rect x="494" y="616" width="112" height="70" rx="4" fill="var(--white)" stroke="var(--red)" stroke-width="2"/>
      <line x1="550" y1="622" x2="550" y2="664" stroke="var(--red)" stroke-width="1" stroke-dasharray="3 3"/>
      <text class="stat-num" x="522" y="650" text-anchor="middle">117</text>
      <text class="stat-label" x="522" y="662" text-anchor="middle">CALORIES</text>
      <text class="stat-num" x="578" y="650" text-anchor="middle">4.2</text>
      <text class="stat-label" x="578" y="662" text-anchor="middle">CARBS</text>
      <rect x="494" y="668" width="112" height="18" rx="3" fill="var(--red)"/>
      <text class="stat-foot" x="550" y="682" text-anchor="middle">PER SERVING</text>
    </g>

    <rect class="bottom-stripe" x="0" y="708" width="1100" height="32" fill="var(--red)"/>
    <g class="supplement-tab">
      <path d="M 436 740 L 446 700 L 654 700 L 664 740 Z" fill="var(--tab-grey)"/>
      <text class="tab-text" x="550" y="726" text-anchor="middle">DIETARY SUPPLEMENT</text>
    </g>
  </svg>
</main>
</body>
</html>
```